Almond butter sachet and jar for new brand called Fenwick’s Pantry

Design for the front and back of a Almond butter sachet and jar, premium design aimed at the fitness market but still approachable for non gym goers.
The Brand name is Fenwick’s Pantry,
Martin Hale is the founder and a michelin starred chef. We want this to stand out from the crowd as a luxury, natural product for use in the gym as well as on the go, we like the premium look of black as a base colour and red colours as they don’t exist in the market, however they can be a little too bold, Our product is natural with no additives, it is vegan, paleo, keto, friendly, plant based and gluten free and only uses hi-Oleic Nuts and no sweetness or palm oil.
Pictures below of the dot&seed sachet and jar are the exact same style as our sachet and jar. The other product is one we really like the look of which is aimed at the fitness market, we don’t want to be the same but almost a hybrid of the two. Our target market however is the high end fitness community, especially with the sachet.

Target Market(s)

Health and Fitness

Requirements
Must have
• High end look and feel,
Nice to have
• Any unique touches to make it stand out from the crowd

```html
<!DOCTYPE html>
<html lang="en">
<head>
<meta charset="utf-8">
<title>Fenwick’s Pantry – Pure Almond Butter Label</title>
<link href="https://fonts.googleapis.com/css2?family=Montserrat:ital,wght@0,700;0,800;1,800&family=Oswald:wght@300&family=Roboto:wght@400&display=swap" rel="stylesheet">
<style>
  :root {
    --page: #ffffff;
    --label-black: #050505;
    --brand-red: #e8141c;
    --white: #ffffff;
    --almond-light: #d9a26b;
    --almond-dark: #8a4f26;
    --body-grey: #cfcfcf;
  }
  * { margin: 0; padding: 0; box-sizing: border-box; }
  html, body {
    width: 1200px;
    height: 799px;
    overflow: hidden;
    background: var(--page);
  }
  .canvas {
    position: relative;
    width: 1200px;
    height: 799px;
  }
  .label {
    position: absolute;
    left: 100px;
    top: 190px;
    width: 1000px;
    height: 420px;
    background: var(--label-black);
    overflow: hidden;
  }
  .brand-name {
    position: absolute;
    left: 80px;
    top: 80px;
    font-family: "Montserrat", sans-serif;
    font-weight: 800;
    color: var(--white);
    font-size: 60px;
    line-height: 1.02;
  }
  .brand-name span { display: block; }
  .almond-art {
    position: absolute;
    left: 80px;
    top: 290px;
    width: 190px;
    height: 95px;
    border-radius: 50% 45% 50% 40%;
    background: radial-gradient(ellipse at 40% 40%, var(--almond-light), var(--almond-dark));
  }
  .product-name {
    position: absolute;
    left: 285px;
    top: 330px;
    font-family: "Montserrat", sans-serif;
    font-weight: 800;
    color: var(--white);
    font-size: 22px;
    line-height: 1.05;
    transform: rotate(-32deg);
    transform-origin: left top;
    white-space: nowrap;
  }
  .product-name .bang { color: var(--brand-red); }
  .tagline {
    position: absolute;
    right: 290px;
    top: 70px;
    text-align: right;
    color: var(--white);
  }
  .tagline-word {
    display: flex;
    align-items: flex-end;
    justify-content: flex-end;
    gap: 8px;
    font-family: "Montserrat", sans-serif;
    font-style: italic;
    font-weight: 800;
    font-size: 26px;
    line-height: 1;
  }
  .tagline-rule {
    width: 80px;
    height: 2px;
    background: var(--white);
    margin-bottom: 5px;
  }
  .tagline-sub {
    font-family: "Oswald", sans-serif;
    font-weight: 300;
    font-size: 25px;
    letter-spacing: -0.5px;
    line-height: 1.1;
  }
  .info-text {
    position: absolute;
    left: 725px;
    top: 130px;
    width: 150px;
    font-family: "Roboto", sans-serif;
    font-size: 7.5px;
    line-height: 9.5px;
    color: var(--body-grey);
    text-align: justify;
  }
  .net-weight {
    position: absolute;
    left: 520px;
    top: 335px;
    font-family: "Montserrat", sans-serif;
    font-weight: 700;
    font-size: 13px;
    color: var(--white);
  }
</style>
</head>
<body>
<main class="canvas">
  <section class="label">
    <h1 class="brand-name"><span>Fenwick’s</span><span>Pantry</span></h1>
    <div class="almond-art" role="img" aria-label="Illustration of whole and split almonds with green leaves"></div>
    <p class="product-name">PURE ALMOND<br>BUTTER<span class="bang">!!</span></p>
    <div class="tagline">
      <div class="tagline-word"><span class="tagline-rule"></span>natural</div>
      <div class="tagline-sub">SOURCE OF ENERGY</div>
    </div>
    <p class="info-text">Fenwick’s Pantry almond butter is made from whole roasted hi-oleic almonds and nothing else. No added sugar, salt or palm oil. Stir well before use as natural oils may separate. Store in a cool dry place and refrigerate after opening. Enjoy within eight weeks of opening. Vegan, paleo, keto friendly, plant based and gluten free. Ingredients: roasted almonds 100%. Allergy advice: contains nuts. Produced in a facility that handles other tree nuts and peanuts. Spread on toast, blend into shakes or eat straight from the spoon after training. Nutrition per 100g: energy 2555kJ / 614kcal, fat 55g, of which saturates 4.2g, carbohydrate 6.1g, of which sugars 4.4g, fibre 10g, protein 24g, salt 0.01g. Each jar is ground slowly in small batches to keep the flavour rich and the texture smooth. Best before: see lid. Packed in a recyclable jar. Please rinse and recycle after use. Made with care for busy people who train hard and eat well.</p>
    <p class="net-weight">150 GM</p>
  </section>
</main>
</body>
</html>
```